Velmora - 3D medical animations and high end visual content

Our company creates high end visual content and animations for medical global companies.
Our website - www.velmora-studio.example
We would like to have an amazing business card for our CEO that he can use in the following exhebitions he is going to attend.
It is very important that the design will be memorable and diffrent. It has to reflect our brand design (you can have it from our website)
We would like to transmit innovation, prestige, luxury, aesthetics.
The card has to be Double Sided

Target Market(s)

Marketing managers in medical global companys

Industry/Entity Type

It Company

Contact Information for Business Card

Requirements
Nice to have
• It is very important that the design will be memorable and diffrent. It has to reflect our brand design (you can have it from our website)

```html
<!DOCTYPE html>
<html lang="en">
<head>
<meta charset="utf-8">
<title>Velmora — CEO Business Card</title>
<link rel="stylesheet" href="https://fonts.googleapis.com/css2?family=Oswald:wght@300;400&family=Open+Sans:wght@400;600&display=swap">
<style>
  :root {
    --page: #e9e9e7;
    --card: #fbfbfa;
    --band-dark: #151515;
    --band-mid: #2c2c2c;
    --ink: #3a3a3a;
    --ink-soft: #6d6d6d;
    --rule: #8a8a8a;
    --white: #ffffff;
  }
  * { margin: 0; padding: 0; box-sizing: border-box; }
  html, body { width: 1200px; height: 1000px; overflow: hidden; }
  body {
    background: var(--page);
    font-family: "Open Sans", Arial, sans-serif;
    position: relative;
  }
  .card {
    position: absolute;
    left: 220px;
    width: 760px;
    height: 434px;
    background: var(--card);
    box-shadow: 0 6px 18px rgba(0,0,0,0.12);
    overflow: hidden;
  }
  .card--front { top: 46px; }
  .card--back { top: 520px; }

  /* Front */
  .brand-band {
    position: absolute;
    left: 0; right: 0;
    top: 120px; height: 194px;
    background: linear-gradient(100deg, var(--band-dark) 0%, var(--band-mid) 50%, var(--band-dark) 100%);
    display: flex; align-items: center; justify-content: center;
  }
  .brand-lockup { position: relative; text-align: center; }
  .brand-lockup__name {
    font-family: "Open Sans", Arial, sans-serif;
    font-weight: 600;
    font-size: 50px;
    letter-spacing: 4px;
    color: var(--white);
    line-height: 1;
  }
  .brand-lockup__rule {
    height: 1px; background: var(--white); opacity: 0.8;
    margin-top: 14px; width: 100%;
  }

  /* Back */
  .back-logo {
    position: absolute; top: 42px; left: 0; right: 0;
    text-align: center;
    font-weight: 600; font-size: 24px; letter-spacing: 2px;
    color: var(--ink);
  }
  .back-rule {
    position: absolute; left: 70px; right: 70px; height: 1px;
    background: var(--rule);
  }
  .back-rule--top { top: 92px; }
  .back-rule--bottom { top: 388px; }
  .person { position: absolute; top: 118px; left: 0; right: 0; text-align: center; }
  .person__name {
    font-family: "Oswald", "Arial Narrow", sans-serif;
    font-weight: 400; font-size: 52px; letter-spacing: 1px;
    color: var(--ink-soft); line-height: 1.1;
  }
  .person__title {
    font-family: "Oswald", "Arial Narrow", sans-serif;
    font-weight: 300; font-size: 20px; letter-spacing: 3px;
    color: var(--ink-soft); margin-top: 4px;
  }
  .contacts {
    position: absolute; top: 262px; left: 70px; right: 70px;
    display: flex; justify-content: space-between;
  }
  .contacts__col { display: flex; flex-direction: column; gap: 22px; }
  .contact { display: flex; align-items: center; gap: 14px; font-size: 15px; color: var(--ink); }
  .contact svg { width: 26px; height: 26px; flex: none; }
</style>
</head>
<body>

<section class="card card--front" aria-label="Card front">
  <div class="brand-band">
    <div class="brand-lockup">
      <div class="brand-lockup__name">VELMORA</div>
      <div class="brand-lockup__rule"></div>
    </div>
  </div>
</section>

<section class="card card--back" aria-label="Card back">
  <div class="back-logo">VELMORA</div>
  <div class="back-rule back-rule--top"></div>

  <div class="person">
    <div class="person__name">LIOR KESSEM</div>
    <div class="person__title">FOUNDER &amp; CEO</div>
  </div>

  <div class="contacts">
    <div class="contacts__col">
      <div class="contact">
        <svg viewBox="0 0 26 26" aria-hidden="true">
          <circle cx="13" cy="13" r="12" fill="none" stroke="#555" stroke-width="1.2"/>
          <rect x="9.5" y="6.5" width="7" height="13" rx="1.2" fill="none" stroke="#555" stroke-width="1.3"/>
          <circle cx="13" cy="17" r="0.9" fill="#555"/>
        </svg>
        <span>+972-50-0001234</span>
      </div>
      <div class="contact">
        <svg viewBox="0 0 26 26" aria-hidden="true">
          <circle cx="13" cy="13" r="12" fill="none" stroke="#555" stroke-width="1.2"/>
          <path d="M9 7.5c-1 .8-1.5 2-1 3.5 1.2 3.3 3.7 5.8 7 7 1.5.5 2.7 0 3.5-1l-2.2-2.2-1.8.9c-1.5-.7-2.7-1.9-3.4-3.4l.9-1.8z" fill="#555"/>
        </svg>
        <span>+972-70-0005678</span>
      </div>
    </div>
    <div class="contacts__col">
      <div class="contact">
        <svg viewBox="0 0 26 26" aria-hidden="true">
          <circle cx="13" cy="13" r="12" fill="none" stroke="#555" stroke-width="1.2"/>
          <rect x="7" y="8.5" width="12" height="9" fill="none" stroke="#555" stroke-width="1.3"/>
          <path d="M7 8.5l6 5 6-5" fill="none" stroke="#555" stroke-width="1.3"/>
        </svg>
        <span>lior@velmora-studio.example</span>
      </div>
      <div class="contact">
        <svg viewBox="0 0 26 26" aria-hidden="true">
          <circle cx="13" cy="13" r="12" fill="none" stroke="#555" stroke-width="1.2"/>
          <circle cx="13" cy="13" r="6.5" fill="none" stroke="#555" stroke-width="1.2"/>
          <ellipse cx="13" cy="13" rx="2.8" ry="6.5" fill="none" stroke="#555" stroke-width="1.1"/>
          <path d="M6.5 13h13" stroke="#555" stroke-width="1.1"/>
        </svg>
        <span>www.velmora-studio.example</span>
      </div>
    </div>
  </div>

  <div class="back-rule back-rule--bottom"></div>
</section>

</body>
</html>
```